Window Perf design with eadership quotes

I am wanting to create a window perf that covers windows in a conference room. I have included a picture of the windows. Each window is 26 1/2 inches by 92 inches. I have also included several other pictures to give an example of how I would like the Quotes to look.

Some Quotes I would like to use
1. Your Future is created by what you do today not tomorrow.
2. The answer is Yes
3. People don't care how much you know until they know how much you care.
4. Treat employees like they make a difference and they will.
5. Don't follow the crowd, Let the crowd follow you.
6. Treat people as if they were what they ought to be , and help them become what they are capable of being.
7. Leadership is not a title, its a behavior. LIVE IT
8. We make a living by what we get, We make a life by what we give.
9. Success is not final, failure is not fatal: it is courage to continue that counts.
10. The best way to predict your future is to create it.
11. The supreme quality of leadership is Integrity.
12. Whatever you are, Be a good one

Quotes

• I am imore interested in how this looks rather than including all of the quotes. I also ant this to be a solid background design for privacy.

```html
<!DOCTYPE html>
<html lang="en">
<head>
<meta charset="utf-8">
<title>Leadership Quotes – Window Perf Layout</title>
<link rel="stylesheet" href="https://fonts.googleapis.com/css2?family=Alegreya&family=Alfa+Slab+One&family=Archivo+Black&family=Baloo+2:wght@500;800&family=Dancing+Script:wght@500;700&family=Kaushan+Script&family=Nunito:wght@800&family=Open+Sans&family=Oswald:wght@500;700&family=Signika&family=Varela+Round&display=swap">
<style>
  :root {
    --frame: #333333;
    --paper: #ffffff;
    --panel: #b3b3b3;
    --ink-light: #e6e6e6;
    --ink-dark: #808080;
    --ink-text: #1a1a1a;
    --k10: #e6e6e6;
    --k30: #b3b3b3;
    --k50: #808080;
  }
  html, body {
    margin: 0;
    padding: 0;
    overflow: hidden;
    background: var(--paper);
  }
  .sheet {
    position: relative;
    width: 1200px;
    height: 849px;
    overflow: hidden;
    background: var(--paper);
    font-family: Arial, Helvetica, sans-serif;
  }
  .sheet-frame {
    position: absolute;
    inset: 0;
  }
  .panel {
    position: absolute;
    top: 85px;
    width: 181px;
    height: 628px;
    background: var(--panel);
  }
  .panel-gap {
    position: absolute;
    top: 85px;
    width: 9px;
    height: 628px;
    background: var(--paper);
    z-index: 3;
  }
  .quote {
    position: absolute;
    margin: 0;
    line-height: 1;
    white-space: nowrap;
    z-index: 2;
  }
  .light { color: var(--ink-light); }
  .dark { color: var(--ink-dark); }

  .rounded { font-family: "Varela Round", sans-serif; letter-spacing: 0.5px; }
  .rounded-bold { font-family: "Nunito", sans-serif; font-weight: 800; }
  .slab { font-family: "Alfa Slab One", serif; letter-spacing: 1px; }
  .friendly { font-family: "Baloo 2", sans-serif; font-weight: 500; }
  .playful { font-family: "Baloo 2", sans-serif; font-weight: 800; }
  .brush { font-family: "Kaushan Script", cursive; }
  .script { font-family: "Dancing Script", cursive; font-weight: 500; }
  .script-bold { font-family: "Dancing Script", cursive; font-weight: 700; }
  .headline { font-family: "Open Sans", sans-serif; }
  .humanist { font-family: "Signika", sans-serif; letter-spacing: 1.5px; }
  .condensed { font-family: "Oswald", sans-serif; font-weight: 500; letter-spacing: -0.3px; }
  .condensed-bold { font-family: "Oswald", sans-serif; font-weight: 700; }
  .serif { font-family: "Alegreya", serif; }
  .heavy { font-family: "Archivo Black", sans-serif; }

  .dimension-label {
    position: absolute;
    font-size: 14px;
    color: var(--ink-text);
    line-height: 1;
  }
  .dimension-label.height {
    transform: rotate(-90deg);
    transform-origin: left top;
  }
  .legend-label {
    position: absolute;
    left: 922px;
    font-size: 15px;
    color: var(--ink-text);
    line-height: 1;
  }
  .brief-note {
    position: absolute;
    left: 123px;
    top: 741px;
    margin: 0;
    font-size: 14px;
    line-height: 17px;
    color: var(--ink-text);
  }
</style>
</head>
<body>
<main class="sheet">
  <svg class="sheet-frame" width="1200" height="849" viewBox="0 0 1200 849" aria-hidden="true">
    <path d="M52 14 H1186 V834 H14 V52 A38 38 0 0 1 52 14 Z" fill="none" stroke="var(--frame)" stroke-width="8"/>
    <path d="M850 838 V795 A46 46 0 0 1 896 749 H1190 V838 Z" fill="var(--frame)"/>
    <g stroke="var(--ink-text)" stroke-width="1">
      <line x1="116" y1="62" x2="297" y2="62"/>
      <line x1="116" y1="56" x2="116" y2="68"/>
      <line x1="297" y1="56" x2="297" y2="68"/>
      <line x1="90" y1="85" x2="90" y2="713"/>
      <line x1="84" y1="85" x2="96" y2="85"/>
      <line x1="84" y1="713" x2="96" y2="713"/>
    </g>
    <circle cx="898" cy="613" r="15" fill="var(--k10)"/>
    <circle cx="898" cy="656" r="15" fill="var(--k30)"/>
    <circle cx="898" cy="699" r="15" fill="var(--k50)"/>
  </svg>

  <span class="dimension-label" style="left:168px;top:41px;">26.5 inches</span>
  <span class="dimension-label height" style="left:68px;top:432px;">92 inches</span>

  <div class="panel" style="left:116px;"></div>
  <div class="panel" style="left:306px;"></div>
  <div class="panel" style="left:496px;"></div>
  <div class="panel" style="left:686px;"></div>
  <div class="panel-gap" style="left:297px;"></div>
  <div class="panel-gap" style="left:487px;"></div>
  <div class="panel-gap" style="left:677px;"></div>

  <!-- Panel one -->
  <p class="quote rounded-bold light" style="left:128px;top:110px;font-size:27px;letter-spacing:1px;">success</p>
  <p class="quote rounded dark" style="left:206px;top:142px;font-size:12px;">is not final</p>
  <p class="quote rounded-bold light" style="left:126px;top:157px;font-size:28px;letter-spacing:1.5px;">failure</p>
  <p class="quote rounded dark" style="left:218px;top:193px;font-size:12px;">is not fatal</p>
  <p class="quote rounded dark" style="left:121px;top:225px;font-size:11px;">It is</p>
  <p class="quote rounded-bold light" style="left:159px;top:209px;font-size:27px;letter-spacing:1px;">courage</p>
  <p class="quote rounded dark" style="left:270px;top:225px;font-size:12px;">to</p>
  <p class="quote rounded dark" style="left:148px;top:250px;font-size:11px;">continue that counts.</p>

  <p class="quote rounded-bold dark" style="left:134px;top:303px;font-size:21px;">leadership</p>
  <p class="quote rounded dark" style="left:163px;top:324px;font-size:7px;">is not a title</p>
  <p class="quote rounded dark" style="left:133px;top:346px;font-size:7px;">its a</p>
  <p class="quote rounded-bold dark" style="left:158px;top:332px;font-size:24px;">behaviour</p>
  <p class="quote slab light" style="left:127px;top:362px;font-size:38px;">LIVE IT</p>

  <p class="quote friendly light" style="left:151px;top:441px;font-size:21px;">The</p>
  <p class="quote friendly light" style="left:190px;top:452px;font-size:21px;">best way</p>
  <p class="quote friendly light" style="left:128px;top:477px;font-size:21px;">to</p>
  <p class="quote friendly light" style="left:152px;top:476px;font-size:21px;">predict</p>
  <p class="quote friendly light" style="left:243px;top:477px;font-size:21px;">your</p>
  <p class="quote brush light" style="left:186px;top:498px;font-size:33px;">future</p>
  <p class="quote friendly light" style="left:139px;top:527px;font-size:18px;">is</p>
  <p class="quote friendly light" style="left:164px;top:535px;font-size:17px;">to</p>
  <p class="quote brush light" style="left:133px;top:540px;font-size:34px;">create</p>
  <p class="quote brush light" style="left:224px;top:556px;font-size:26px;">it.</p>

  <p class="quote script dark" style="left:131px;top:631px;font-size:38px;">Dont</p>
  <p class="quote script dark" style="left:207px;top:656px;font-size:33px;">follow</p>

  <!-- Panels two and three -->
  <p class="quote headline light" style="left:310px;top:98px;font-size:88px;letter-spacing:11px;">PEOPLE</p>
  <p class="quote humanist dark" style="left:352px;top:139px;font-size:22px;">don’t</p>
  <p class="quote condensed-bold dark" style="left:428px;top:128px;font-size:30px;">care</p>
  <p class="quote humanist dark" style="left:504px;top:139px;font-size:22px;">how much</p>
  <p class="quote humanist dark" style="left:360px;top:172px;font-size:22px;">you know</p>
  <p class="quote humanist dark" style="left:505px;top:172px;font-size:22px;">until they</p>
  <p class="quote humanist dark" style="left:352px;top:204px;font-size:22px;">know how</p>
  <p class="quote humanist dark" style="left:503px;top:204px;font-size:22px;">much you</p>
  <p class="quote condensed-bold dark" style="left:426px;top:226px;font-size:32px;">care</p>

  <p class="quote serif dark" style="left:316px;top:309px;font-size:28px;">Your</p>
  <p class="quote script-bold light" style="left:366px;top:274px;font-size:90px;">Future</p>
  <p class="quote serif dark" style="left:546px;top:364px;font-size:29px;">is created</p>
  <p class="quote serif dark" style="left:380px;top:405px;font-size:31px;">by what</p>
  <p class="quote serif dark" style="left:498px;top:405px;font-size:31px;">you do</p>
  <p class="quote headline light" style="left:520px;top:442px;font-size:46px;">‘today’</p>
  <p class="quote serif dark" style="left:504px;top:502px;font-size:31px;">not</p>
  <p class="quote headline light" style="left:388px;top:535px;font-size:46px;">‘tomorrow’.</p>

  <p class="quote brush dark" style="left:312px;top:672px;font-size:24px;">the</p>
  <p class="quote brush light" style="left:350px;top:620px;font-size:48px;">crowd</p>
  <p class="quote script dark" style="left:512px;top:618px;font-size:40px;">Let</p>
  <p class="quote script dark" style="left:557px;top:652px;font-size:29px;">the crowd</p>

  <!-- Panel four -->
  <p class="quote playful light" style="left:696px;top:116px;font-size:34px;">Whatever</p>
  <p class="quote serif dark" style="left:788px;top:155px;font-size:29px;">you</p>
  <p class="quote serif dark" style="left:812px;top:180px;font-size:29px;">are,</p>
  <p class="quote serif dark" style="left:708px;top:188px;font-size:31px;">Be a</p>
  <p class="quote playful light" style="left:737px;top:206px;font-size:44px;">good</p>
  <p class="quote serif dark" style="left:768px;top:255px;font-size:29px;">one.</p>

  <p class="quote condensed dark" style="left:702px;top:320px;font-size:19px;">The supreme quality</p>
  <p class="quote condensed dark" style="left:718px;top:348px;font-size:19px;">of leadership is</p>
  <p class="quote rounded-bold light" style="left:708px;top:380px;font-size:27px;letter-spacing:2px;">integrity.</p>

  <p class="quote condensed-bold light" style="left:713px;top:448px;font-size:25px;">‘the</p>
  <p class="quote condensed-bold dark" style="left:742px;top:465px;font-size:24px;">answer</p>
  <p class="quote condensed-bold dark" style="left:771px;top:489px;font-size:23px;">is</p>
  <p class="quote heavy light" style="left:714px;top:512px;font-size:52px;">YES’</p>

  <p class="quote script light" style="left:700px;top:596px;font-size:58px;">follow</p>
  <p class="quote script dark" style="left:808px;top:658px;font-size:28px;">you</p>

  <span class="legend-label" style="top:606px;">C:0 Y:0 M:0 K:10</span>
  <span class="legend-label" style="top:649px;">C:0 Y:0 M:0 K:30</span>
  <span class="legend-label" style="top:692px;">C:0 Y:0 M:0 K:50</span>

  <p class="brief-note">Digitally printed opaque vinyl decals to be applied to both sides of the window.<br>Showing quotes to both the office and conference room.</p>
</main>
</body>
</html>
```